Organic Herbs & Spices container

Greek startup company, which cultivate and trade spices and herbs (such as oregano, mint, thyme, sage etc.)

At present we are interested in only the type and shape of packaging which should be made by materials such as paper, cardboard, laminated paper and others based on paper or plastic.

Package size vary from 80g (2.82oz) - 300g (10.58oz). We are going to use the same packing for a variety of products with different information

* Please find attached our logo which should be included in the design.
* There is no company name available at the moment, however a name placeholder should be included.
* include a placeholder for the type of product (sage, oregano, mint, tea etc...).
* Each package should have a place in order to include product details and nutrition facts.

e.g.
xxxx (company name placeholder)
Sage (product type)
product details and nutrition facts.
Updates

Dear designers,first of all, thank you for your proposals. Please find bellow some updates for the project.- It is mandatory to include the logo into the design - Each package should be able to stored vertically - We are looking for one specific package design, please do not submit many variations of a certain package neither colour differentiations Thanks and good luck Added Wednesday, September 28, 2016

Please avoid the use of images. The same package will be used for all the kinds of products (only name and maybe colour will be different among different products. A transparent frame that will show the contents could be used too) Added Wednesday, September 28, 2016

Please find attached logo in EPS format

Our logo is the baseline, any concepts should be based on it. Try to avoid just adding the logo as a small sticker somewhere on the design. Please try to create around it at any way toy like. This could be, to visualize it as a 3D shape or object which can be used as the container of the products.

Reason: We would like to extend the time of the project. We believe that most of the submitted designs do not comply with our requirements.

Reason: We would like to see a bigger variety of ideas

Target Market(s)

Pretty much to anyone over 20 years old worldwide.

Industry/Entity Type

Nutrition

Requirements
Must have
• It should be attractive, easily recognized, simple yet innovative, durable, functional (easy to use) and easy to store.
Should not have
• Project must not include complex or obnoxious shapes and colours.

```html
<!DOCTYPE html>
<html lang="en">
<head>
<meta charset="utf-8">
<title>Greek Spices – Carton Panels</title>
<link rel="stylesheet" href="https://fonts.googleapis.com/css2?family=EB+Garamond:ital,wght@0,500;1,400;1,500&family=Arimo:wght@400&display=swap">
<style>
  :root {
    --aegean: #1b63c2;
    --aegean-deep: #1556ad;
    --aegean-soft: #dce9f9;
    --aegean-mist: #edf3fb;
    --panel: #f4f4f4;
    --page: #ffffff;
    --edge: #dcdcdc;
  }
  * { box-sizing: border-box; margin: 0; padding: 0; }
  html, body { width: 1200px; height: 1200px; overflow: hidden; background: var(--page); }
  .canvas { position: relative; width: 1200px; height: 1200px; }

  .panel {
    position: absolute;
    background: var(--panel);
    border: 1px solid var(--edge);
    overflow: hidden;
  }
  .panel--front { left: 40px; top: 160px; width: 340px; height: 900px; }
  .panel--side  { left: 420px; top: 160px; width: 340px; height: 900px; }
  .panel--lid   { left: 800px; top: 160px; width: 340px; height: 340px; background: var(--aegean); border-color: var(--aegean-deep); }

  .border-band {
    position: absolute; left: 0; top: 0; width: 100%; height: 120px;
    background: linear-gradient(180deg, var(--aegean) 0 14px, #3f86d8 14px 106px, var(--aegean) 106px);
  }

  .region-map {
    position: absolute; left: 30px; top: 200px; width: 280px; height: 280px;
    background: radial-gradient(ellipse at 45% 45%, var(--aegean) 0 40%, #5a95dc 70%, var(--panel) 100%);
  }

  .title-greek {
    position: absolute; left: 0; right: 0; top: 500px;
    text-align: center;
    font-family: "EB Garamond", serif;
    font-style: italic; font-weight: 500;
    font-size: 28px; line-height: 36px;
    color: var(--aegean);
  }

  .product-info {
    position: absolute; left: 0; right: 0; top: 640px;
    text-align: center;
    font-family: "Arimo", sans-serif;
    color: var(--aegean);
    letter-spacing: 0.12em;
  }
  .product-type { font-size: 18px; line-height: 22px; margin-bottom: 14px; }
  .storage { font-size: 16px; line-height: 21px; margin-bottom: 12px; }
  .best-before { font-size: 16px; margin-bottom: 34px; }
  .net-weight { font-size: 23px; letter-spacing: 0.14em; }

  .temple-frame {
    position: absolute; left: 20px; top: 150px; width: 300px; height: 730px;
    background: linear-gradient(180deg, var(--aegean-soft) 0%, var(--aegean-mist) 50%, var(--aegean-soft) 100%);
  }
  .temple-text {
    position: absolute; left: 60px; right: 60px; top: 380px;
    text-align: center;
    font-family: "EB Garamond", serif;
    font-style: italic; font-weight: 400;
    font-size: 25px; line-height: 40px;
    color: var(--aegean);
  }

  .brand {
    position: absolute; left: 0; right: 0; top: 50%;
    transform: translateY(-50%);
    display: flex; align-items: center; justify-content: center; gap: 14px;
    font-family: "EB Garamond", serif;
    font-weight: 500; font-size: 30px;
    color: var(--page);
  }
  .brand-dot { width: 22px; height: 22px; border-radius: 50%; background: var(--page); }
</style>
</head>
<body>
<main class="canvas">

  <section class="panel panel--front">
    <div class="border-band" role="img" aria-label="Band of white palmette ornaments on blue"></div>
    <div class="region-map" role="img" aria-label="Blue silhouette map of Greece and its islands"></div>
    <h1 class="title-greek" lang="el">ελληνικά<br>Μπαχαρικά</h1>
    <div class="product-info">
      <p class="product-type">DRIED<br>COARSE<br>NUTMEG</p>
      <p class="storage">Store in a cool dry<br>place away from<br>direct sunlight</p>
      <p class="best-before">Best Before</p>
      <p class="net-weight">80g (2.82oz)</p>
    </div>
  </section>

  <section class="panel panel--side">
    <div class="border-band" role="img" aria-label="Band of white palmette ornaments on blue"></div>
    <div class="temple-frame" role="img" aria-label="Blue line drawing of a Greek temple front with pediment and two Ionic columns framing the text"></div>
    <p class="temple-text">The Simplicity<br>and traditional<br>rustic goodness<br>of Greek Spices,<br>renowned the<br>world over<br>presented to you<br>here in this<br>package.<br>(sample text)</p>
  </section>

  <section class="panel panel--lid">
    <div class="brand"><span class="brand-dot"></span><span>Aegean Grove</span></div>
  </section>

</main>
</body>
</html>
```